Web Page Design for a Website that Provides Tutoring

I am looking to create an online tutoring website. The website will allow parents or students to contact tutors with a view to instructing them to tutor themselves or their children.

The name of the website is LendYourLessons.

This brief is to create the design for one of the web pages for this web site. I am hoping the same designer will be available to design other pages.

The page I want designed is one of the more complex and I have attached the design as an excel spreadsheet. The web page needs to include all the items on this page but if you want to change the positioning of the items then Im fine with that.

I recently had two logos created for this website. My favourite is the one with a mortar board but im not sure I like the colours. I have attached both of these logos and you can use either of them, change the colours or create something different. I just want a design pleasing to the eye. If the logo is changed I would like that in a seperate file.

So can you please submit designs for this page. I have attached the two logos which you can use, change or if you feel you have a better idea then you can use that.

On the spreadsheet the Send Message, Favourite etc are buttons.

Target Market(s)

People who want to better themselves.
Possible middle class to upper class.

Industry/Entity Type

Tutoring

Number of Pages Required

1 page

Requirements
Must have
• The designs must have alot of the information attached in the spreadsheet.

```html
<!DOCTYPE html>
<html lang="en">
<head>
<meta charset="utf-8">
<title>LendYourLessons – Tutor Profile</title>
<link href="https://fonts.googleapis.com/css2?family=Open+Sans:ital,wght@0,400;0,600;0,700;1,400&display=swap" rel="stylesheet">
<style>
:root{
  --dark:#393830;
  --coral:#f47b5e;
  --orange:#f7a21b;
  --amber:#f08c1e;
  --olive:#a2a237;
  --blue:#1fa1d6;
  --text:#333333;
  --muted:#8d8d8d;
  --line:#d9d9d9;
  --panel:#f0f0f2;
  --cell:#f2efe9;
  --white:#ffffff;
  --star-off:#cfcfcf;
}
*{box-sizing:border-box;margin:0;padding:0}
html,body{width:1200px;height:2605px;overflow:hidden}
body{font-family:"Open Sans",Arial,sans-serif;color:var(--text);background:var(--white)}
.page{position:relative;width:1200px;height:2605px}
.abs{position:absolute}

/* header */
.site-header{left:0;top:0;width:1200px;height:221px;background:var(--dark)}
.brand{left:0;top:50px;width:1200px;text-align:center;font-size:44px;font-weight:700;color:var(--white);letter-spacing:-0.5px}
.main-nav{left:0;top:148px;width:1200px;height:30px}
.main-nav a{position:absolute;top:0;transform:translateX(-50%);font-size:14px;letter-spacing:.5px;color:#c9c9c4;text-decoration:none;white-space:nowrap}
.main-nav a.active{color:var(--coral);font-weight:700}
.main-nav a.active::after{content:"";position:absolute;left:0;right:0;top:24px;height:2px;background:var(--coral)}
.main-nav a.active::before{content:"";position:absolute;left:50%;top:26px;margin-left:-4px;border:4px solid transparent;border-top-color:var(--coral)}

/* profile */
.profile-photo{left:94px;top:259px;width:224px;height:226px;border:2px solid #e6e6e6;box-shadow:2px 3px 4px rgba(0,0,0,.18);background:linear-gradient(160deg,#efe9e4 0%,#c9a996 45%,#6e4d3c 100%)}
.facts{left:94px;top:508px;width:230px}
.fact{position:relative;height:35px}
.fact-label{position:absolute;left:0;top:2px;font-size:11px;font-weight:700;color:var(--text);letter-spacing:.3px}
.fact-value{position:absolute;left:127px;top:0;width:95px;height:16px;background:var(--coral);color:var(--white);font-size:10px;line-height:16px;text-align:center;letter-spacing:.3px}
.check-badge{left:94px;top:655px;width:73px;height:50px;border:2px solid var(--coral);border-radius:3px;background:var(--white)}

.tutor-name{left:375px;top:268px;font-size:29px;font-weight:700;color:var(--text)}
.tutor-name .first{color:var(--coral)}
.last-active{left:519px;top:284px;font-size:11px;font-style:italic;color:var(--muted)}
.action-btn{top:271px;width:34px;height:30px;border-radius:3px;background:var(--coral);display:flex;align-items:center;justify-content:center}
.divider{height:1px;background:var(--line)}

.rating{top:360px;width:180px;text-align:center}
.rating-label{font-size:17px;color:var(--text)}
.rating svg{display:block;margin:13px auto 6px}
.rating-value{font-size:20px;font-weight:700}
.bio{left:399px;top:499px;width:707px;font-size:13.5px;line-height:35px;color:var(--muted);text-align:justify}

/* sections */
.band{left:0;width:1200px}
.band.grey{background:var(--panel)}
.section-title{font-size:29px;font-weight:700;color:var(--text)}
.section-title .accent{color:var(--coral)}

/* subjects table */
.subjects{left:108px;top:926px;width:983px;border-collapse:collapse;background:var(--white)}
.subjects th{height:45px;background:var(--coral);color:var(--white);font-size:16px;font-weight:600;border-right:3px solid var(--panel)}
.subjects th:last-child,.subjects td:last-child{border-right:0}
.subjects td{height:73px;text-align:center;font-size:19px;font-weight:700;border-right:2px solid #e9e9e9;vertical-align:middle}
.subjects tr.first td{padding-top:40px;height:113px}
.subjects tr.last td{padding-bottom:40px;height:113px}
.chem{color:var(--amber)}
.bio-price{color:var(--olive)}
.subject-tag{display:flex;align-items:center;justify-content:center;gap:10px;width:156px;height:42px;margin-left:3px;border-radius:2px;color:var(--white);font-size:16px;font-weight:700;letter-spacing:.3px}
.subject-tag.chemistry{background:var(--orange)}
.subject-tag.biology{background:var(--olive)}

/* schedule */
.week-nav{left:280px;top:1383px;width:340px;display:flex;justify-content:space-between;align-items:center;color:var(--coral)}
.week-nav .label{font-size:22px;font-weight:600;letter-spacing:1.5px}
.day{top:1437px;width:72px;text-align:center;font-size:16px;color:var(--text)}
.slot-label{left:70px;width:112px;text-align:right;font-size:14px;color:var(--text)}
.calendar{left:196px;top:1478px;width:504px;height:361px;border-top:5px solid var(--coral);display:grid;grid-template-columns:repeat(7,72px);grid-template-rows:repeat(5,71.2px)}
.cell{background:var(--cell);border:1px solid var(--white)}
.cell.taken{background:var(--coral)}
.cell.reserved{background:var(--orange)}
.cell.holiday{background:var(--olive)}
.cell.unavailable{background:var(--blue)}
.legend{top:1882px;font-size:14px;color:var(--text);display:flex;align-items:center;gap:12px}
.legend i{display:block;width:10px;height:10px}
.btn{left:781px;width:282px;height:54px;display:flex;align-items:center;justify-content:center;font-size:16px;border-radius:2px}
.btn.primary{background:var(--coral);color:var(--white);border:1px solid #e0674a}
.btn.secondary{background:var(--white);color:var(--coral);border:1px solid var(--coral)}
.or{left:781px;top:1645px;width:282px;text-align:center;font-size:16px;color:var(--muted)}

/* reviews */
.reviews-summary{left:104px;top:2096px;font-size:14px;font-style:italic;color:#6f6f6f}
.review{width:397px;background:var(--white);box-shadow:0 1px 4px rgba(0,0,0,.15)}
.review::after{content:"";position:absolute;left:44px;bottom:-18px;border-left:0 solid transparent;border-right:22px solid transparent;border-top:18px solid var(--white);filter:drop-shadow(0 2px 1px rgba(0,0,0,.08))}
.review-avatar{position:absolute;left:12px;top:18px;width:52px;height:40px;border-radius:50%;background:#f7bfae}
.review-head{position:absolute;left:84px;top:16px;display:flex;align-items:center;gap:14px}
.review-name{font-size:19px;font-weight:700;color:var(--text)}
.review-name .first{color:var(--amber)}
.review-text{position:absolute;left:84px;top:56px;width:292px;font-size:13.5px;line-height:19.5px;color:#666}
.review-time{position:absolute;right:14px;bottom:12px;font-size:15px;color:var(--muted)}

.site-footer{left:0;top:2582px;width:1200px;height:23px;background:var(--dark);color:#a9a9a2;font-size:9px;line-height:23px;text-align:center}
</style>
</head>
<body>
<svg width="0" height="0" style="position:absolute" aria-hidden="true">
  <defs>
    <symbol id="star" viewBox="0 0 20 20"><polygon points="10,1 12.6,7 19,7.4 14,11.6 15.6,18 10,14.5 4.4,18 6,11.6 1,7.4 7.4,7"/></symbol>
  </defs>
</svg>

<div class="page">

  <header class="abs site-header">
    <div class="abs brand">LendYourLessons</div>
    <nav class="abs main-nav">
      <a href="#" style="left:257px">HOME</a>
      <a href="#" class="active" style="left:346px">SEARCH</a>
      <a href="#" style="left:446px">STUDENT</a>
      <a href="#" style="left:542px">TUTOR</a>
      <a href="#" style="left:632px">ABOUT</a>
      <a href="#" style="left:729px">CONTACT</a>
      <a href="#" style="left:830px">SIGN IN</a>
      <a href="#" style="left:931px">REGISTER</a>
    </nav>
  </header>

  <!-- tutor profile -->
  <section>
    <div class="abs profile-photo" role="img" aria-label="Portrait photo of the tutor"></div>

    <dl class="abs facts">
      <div class="fact"><dt class="fact-label">TUTORING TYPE</dt><dd class="fact-value">PERSONAL</dd></div>
      <div class="fact"><dt class="fact-label">WILLING TO TRAVEL</dt><dd class="fact-value">HOME ONLY</dd></div>
      <div class="fact"><dt class="fact-label">AGE</dt><dd class="fact-value">20 YEARS OLD</dd></div>
      <div class="fact"><dt class="fact-label">MEMBER SINCE</dt><dd class="fact-value">DEC 2016</dd></div>
    </dl>
    <div class="abs check-badge" role="img" aria-label="Background check badge"></div>

    <h1 class="abs tutor-name"><span class="first">Jane</span> Doe</h1>
    <div class="abs last-active">active 15 minutes ago</div>

    <a class="abs action-btn" style="left:948px" aria-label="Send message">
      <svg width="18" height="13" viewBox="0 0 18 13"><rect x="1" y="1" width="16" height="11" fill="none" stroke="#fff" stroke-width="1.6"/><polyline points="1,1 9,7.5 17,1" fill="none" stroke="#fff" stroke-width="1.6"/></svg>
    </a>
    <a class="abs action-btn" style="left:1011px" aria-label="Add to favourites">
      <svg width="18" height="18" fill="#fff"><use href="#star"/></svg>
    </a>
    <a class="abs action-btn" style="left:1072px" aria-label="Write a review">
      <svg width="20" height="16" viewBox="0 0 20 16"><path d="M10 1C5 1 1 3.8 1 7.3c0 2 1.3 3.8 3.4 4.9L3.6 15l4-2.2c.8.2 1.6.3 2.4.3 5 0 9-2.8 9-6.3S15 1 10 1z" fill="#fff"/></svg>
    </a>

    <div class="abs divider" style="left:368px;top:332px;width:738px"></div>

    <div class="abs rating" style="left:400px">
      <div class="rating-label">Review Score</div>
      <svg width="93" height="17" fill="var(--star-off)">
        <use href="#star" x="0" width="17" height="17"/><use href="#star" x="19" width="17" height="17"/><use href="#star" x="38" width="17" height="17"/><use href="#star" x="57" width="17" height="17"/><use href="#star" x="76" width="17" height="17"/>
        <svg width="84.5" height="17" fill="var(--amber)"><use href="#star" x="0" width="17" height="17"/><use href="#star" x="19" width="17" height="17"/><use href="#star" x="38" width="17" height="17"/><use href="#star" x="57" width="17" height="17"/><use href="#star" x="76" width="17" height="17"/></svg>
      </svg>
      <div class="rating-value" style="color:var(--amber)">4.5/5</div>
    </div>
    <div class="abs rating" style="left:622px">
      <div class="rating-label">Reliability</div>
      <svg width="93" height="17" fill="var(--star-off)">
        <use href="#star" x="0" width="17" height="17"/><use href="#star" x="19" width="17" height="17"/><use href="#star" x="38" width="17" height="17"/><use href="#star" x="57" width="17" height="17"/><use href="#star" x="76" width="17" height="17"/>
        <svg width="74" height="17" fill="var(--olive)"><use href="#star" x="0" width="17" height="17"/><use href="#star" x="19" width="17" height="17"/><use href="#star" x="38" width="17" height="17"/><use href="#star" x="57" width="17" height="17"/></svg>
      </svg>
      <div class="rating-value" style="color:var(--olive)">4.0/5</div>
    </div>
    <div class="abs rating" style="left:837px">
      <div class="rating-label">Punctuality</div>
      <svg width="93" height="17" fill="var(--star-off)">
        <use href="#star" x="0" width="17" height="17"/><use href="#star" x="19" width="17" height="17"/><use href="#star" x="38" width="17" height="17"/><use href="#star" x="57" width="17" height="17"/><use href="#star" x="76" width="17" height="17"/>
        <svg width="86" height="17" fill="var(--blue)"><use href="#star" x="0" width="17" height="17"/><use href="#star" x="19" width="17" height="17"/><use href="#star" x="38" width="17" height="17"/><use href="#star" x="57" width="17" height="17"/><use href="#star" x="76" width="17" height="17"/></svg>
      </svg>
      <div class="rating-value" style="color:var(--blue)">4.6/5</div>
    </div>

    <p class="abs bio">Lorem ipsum dolor sit amet, consectetur adipiscing elit, sed do eiusmod tempor incididunt ut labore et dolore magna aliqua. Ut enim ad minim veniam, quis nostrud exercitation ullamco laboris nisi ut aliquip ex ea commodo consequat. Duis aute irure dolor in reprehenderit in voluptate velit esse cillum dolore eu fugiat nulla pariatur. Excepteur sint occaecat cupidatat non proident, sunt in culpa qui officia deserunt mollit anim id est laborum.Ut enim ad minim veniam, quis nostrud exercitation ullamco laboris nisi ut aliquip ex ea commodo consequat. Duis aute irure dolor in reprehenderit in voluptate velit esse cillum dolore eu fugiat nulla pariatur.</p>
  </section>

  <!-- subjects -->
  <section class="abs band grey" style="top:773px;height:481px">
    <h2 class="abs section-title" style="left:108px;top:41px"><span class="accent">Subjects</span> Taught</h2>
    <div class="abs divider" style="left:108px;top:111px;width:986px"></div>
    <table class="abs subjects" style="top:153px">
      <colgroup><col style="width:165px"><col style="width:135px"><col style="width:137px"><col style="width:137px"><col style="width:138px"><col style="width:137px"><col style="width:134px"></colgroup>
      <thead><tr><th>Subjects</th><th>Primary</th><th>Secondary</th><th>GCSE</th><th>A- Level</th><th>University</th><th>Adult Learing</th></tr></thead>
      <tbody>
        <tr class="first">
          <td><span class="subject-tag chemistry"><svg width="13" height="17" viewBox="0 0 13 17"><path d="M4.5 1h4M5 1v5L1.5 14.5c-.4 1 .2 1.8 1.2 1.8h7.6c1 0 1.6-.8 1.2-1.8L8 6V1" fill="none" stroke="#fff" stroke-width="1.4"/></svg>CHEMISTRY</span></td>
          <td class="chem">£20</td><td></td><td class="chem">£25</td><td class="chem">£30</td><td></td><td></td>
        </tr>
        <tr class="last">
          <td><span class="subject-tag biology"><svg width="14" height="17" viewBox="0 0 14 17"><path d="M6 1l3 2-4 6-3-2zM4 9.5c4 0 7-2 7-5M1 15.5h12M4 15.5c0-2 1-4 4-5" fill="none" stroke="#fff" stroke-width="1.4"/></svg>BIOLOGY</span></td>
          <td class="bio-price">£20</td><td></td><td class="bio-price">£25</td><td class="bio-price">£30</td><td></td><td></td>
        </tr>
      </tbody>
    </table>
  </section>

  <!-- schedule -->
  <section>
    <h2 class="abs section-title" style="left:106px;top:1290px"><span class="accent">Available</span> Schedule</h2>
    <div class="abs divider" style="left:106px;top:1356px;width:988px"></div>

    <div class="abs week-nav">
      <svg width="10" height="12"><polygon points="9,0 9,12 0,6" fill="var(--coral)"/></svg>
      <span class="label">December 5-11, 2016</span>
      <svg width="10" height="12"><polygon points="1,0 1,12 10,6" fill="var(--coral)"/></svg>
    </div>

    <div class="abs day" style="left:196px">Mon 5</div>
    <div class="abs day" style="left:268px">Tue 6</div>
    <div class="abs day" style="left:340px">Wed 7</div>
    <div class="abs day" style="left:412px">Thu 8</div>
    <div class="abs day" style="left:484px">Fri 9</div>
    <div class="abs day" style="left:556px">Sat 10</div>
    <div class="abs day" style="left:628px">Sun 11</div>

    <div class="abs slot-label" style="top:1510px">4 pm - 5 pm</div>
    <div class="abs slot-label" style="top:1567px">5 pm - 6 pm</div>
    <div class="abs slot-label" style="top:1638px">6 pm - 7 pm</div>
    <div class="abs slot-label" style="top:1709px">7 pm - 8 pm</div>
    <div class="abs slot-label" style="top:1781px">8 pm - 9 pm</div>

    <div class="abs calendar">
      <div class="cell"></div><div class="cell"></div><div class="cell"></div><div class="cell"></div><div class="cell"></div><div class="cell"></div><div class="cell taken"></div>
      <div class="cell unavailable"></div><div class="cell"></div><div class="cell"></div><div class="cell"></div><div class="cell taken"></div><div class="cell"></div><div class="cell"></div>
      <div class="cell"></div><div class="cell"></div><div class="cell taken"></div><div class="cell"></div><div class="cell"></div><div class="cell"></div><div class="cell reserved"></div>
      <div class="cell"></div><div class="cell"></div><div class="cell"></div><div class="cell"></div><div class="cell"></div><div class="cell taken"></div><div class="cell"></div>
      <div class="cell holiday"></div><div class="cell"></div><div class="cell"></div><div class="cell"></div><div class="cell"></div><div class="cell"></div><div class="cell holiday"></div>
    </div>

    <div class="abs legend" style="left:196px"><i style="background:var(--coral)"></i>TAKEN</div>
    <div class="abs legend" style="left:290px"><i style="background:var(--orange)"></i>RESERVED</div>
    <div class="abs legend" style="left:408px"><i style="background:var(--olive)"></i>HOLIDAY</div>
    <div class="abs legend" style="left:521px"><i style="background:var(--blue)"></i>NOT AVAILABLE</div>

    <a class="abs btn primary" style="top:1559px">Set an Appointment</a>
    <div class="abs or">or</div>
    <a class="abs btn secondary" style="top:1702px">Reserve a Date</a>
  </section>

  <!-- reviews -->
  <section class="abs band grey" style="top:1959px;height:623px"></section>
  <h2 class="abs section-title" style="left:104px;top:2003px">Reviews</h2>
  <a class="abs action-btn" style="left:1060px;top:2009px" aria-label="Write a review">
    <svg width="20" height="16" viewBox="0 0 20 16"><path d="M10 1C5 1 1 3.8 1 7.3c0 2 1.3 3.8 3.4 4.9L3.6 15l4-2.2c.8.2 1.6.3 2.4.3 5 0 9-2.8 9-6.3S15 1 10 1z" fill="#fff"/></svg>
  </a>
  <div class="abs divider" style="left:104px;top:2072px;width:990px;background:#d3d3d6"></div>
  <p class="abs reviews-summary">4 reviews with an average rating of 4.0</p>

  <article class="abs review" style="left:174px;top:2159px;height:165px">
    <div class="review-avatar"></div>
    <div class="review-head"><span class="review-name"><span class="first">John</span> Doe</span>
      <svg width="109" height="17" fill="var(--star-off)"><use href="#star" x="0" width="17" height="17"/><use href="#star" x="22" width="17" height="17"/><use href="#star" x="44" width="17" height="17"/><use href="#star" x="66" width="17" height="17"/><use href="#star" x="88" width="17" height="17"/><svg width="84" height="17" fill="var(--amber)"><use href="#star" x="0" width="17" height="17"/><use href="#star" x="22" width="17" height="17"/><use href="#star" x="44" width="17" height="17"/><use href="#star" x="66" width="17" height="17"/></svg></svg>
    </div>
    <p class="review-text">Lorem ipsum dolor sit amet, consectetur adipiscing elit, sed do eiusmod tempor incid-idunt ut labore et dolore magna aliqua.</p>
    <span class="review-time">3 days ago</span>
  </article>

  <article class="abs review" style="left:630px;top:2159px;height:165px">
    <div class="review-avatar"></div>
    <div class="review-head"><span class="review-name"><span class="first">John</span> Doe</span>
      <svg width="109" height="17" fill="var(--star-off)"><use href="#star" x="0" width="17" height="17"/><use href="#star" x="22" width="17" height="17"/><use href="#star" x="44" width="17" height="17"/><use href="#star" x="66" width="17" height="17"/><use href="#star" x="88" width="17" height="17"/><svg width="84" height="17" fill="var(--amber)"><use href="#star" x="0" width="17" height="17"/><use href="#star" x="22" width="17" height="17"/><use href="#star" x="44" width="17" height="17"/><use href="#star" x="66" width="17" height="17"/></svg></svg>
    </div>
    <p class="review-text">Lorem ipsum dolor sit amet, consectetur adipiscing elit, sed do eiusmod tempor incid-idunt ut labore et dolore magna aliqua.</p>
    <span class="review-time">3 days ago</span>
  </article>

  <article class="abs review" style="left:174px;top:2369px;height:150px">
    <div class="review-avatar"></div>
    <div class="review-head"><span class="review-name"><span class="first">Jane</span> Doe</span>
      <svg width="109" height="17" fill="var(--star-off)"><use href="#star" x="0" width="17" height="17"/><use href="#star" x="22" width="17" height="17"/><use href="#star" x="44" width="17" height="17"/><use href="#star" x="66" width="17" height="17"/><use href="#star" x="88" width="17" height="17"/><svg width="84" height="17" fill="var(--amber)"><use href="#star" x="0" width="17" height="17"/><use href="#star" x="22" width="17" height="17"/><use href="#star" x="44" width="17" height="17"/><use href="#star" x="66" width="17" height="17"/></svg></svg>
    </div>
    <p class="review-text">Lorem ipsum dolor sit amet, consectetur adipiscing elit, sed do eiusmod tempor incid-idunt ut labore et dolore magna aliqua.</p>
    <span class="review-time">3 days ago</span>
  </article>

  <article class="abs review" style="left:630px;top:2369px;height:150px">
    <div class="review-avatar"></div>
    <div class="review-head"><span class="review-name"><span class="first">Jane</span> Doe</span>
      <svg width="109" height="17" fill="var(--star-off)"><use href="#star" x="0" width="17" height="17"/><use href="#star" x="22" width="17" height="17"/><use href="#star" x="44" width="17" height="17"/><use href="#star" x="66" width="17" height="17"/><use href="#star" x="88" width="17" height="17"/><svg width="84" height="17" fill="var(--amber)"><use href="#star" x="0" width="17" height="17"/><use href="#star" x="22" width="17" height="17"/><use href="#star" x="44" width="17" height="17"/><use href="#star" x="66" width="17" height="17"/></svg></svg>
    </div>
    <p class="review-text">Lorem ipsum dolor sit amet, consectetur adipiscing elit, sed do eiusmod tempor incid-idunt ut labore et dolore magna aliqua.</p>
    <span class="review-time">3 days ago</span>
  </article>

  <footer class="abs site-footer">Copyright © 2016 LendYourLessons. Use of this website constitutes acceptance of our User Agreement and Privacy Policy.</footer>

</div>
</body>
</html>
```